Express envelope design for courier company

We're a courier company launching a new service for sending documents around Australia. We need a design for the express envelope that will be used to hold the documents during transit. The envelope will be printed in colour on cardboard. Please see brief attached.

Design cues:
• Vibrant
• Simplified
• Clean
• Aesthetically pleasing
• Artistic
• Nothing “institutional” or “Harwick Lines”
• Nothing cramped, no small text

It's fine to crop, recolour, or reinterpret the logo.

Industry/Entity Type

It Company

Font styles to use
Sans Serif

Requirements
Must have
• Dimensions:
• Back side: 350 x 230 mm
• Front side: 387.5 x 230 mm (including flap to close envelope)
• Back side barcode panel: 90 x 75 mm (blank area for adhesive barcode)
• Back side address panel: 150 x 90 mm (see PDF for contents and layout)
• Front side text:
• QM-DR
• Express Envelope
• Send With Trust
• 1300 584 961
• qmdr.com.au
• Back side text:
• For documents
• Max. weight 500g, max width 20mm
• Send With Trust
• • Time-guaranteed and next-flight-out service for vital deliveries
• • Same-day and next-day local services
• • Overnight service to most Australian locations
• • Budget road service Australia-wide
• • Worldwide express courier
• Visit qmdr.com.au or phone 1300 584 961
• Flap text:
• Go to qmdr.com.au to book your pickup.
• Carried subject to QM-DR Standard Conditions of Carriage; see our website.
Nice to have
• Our web colours:
• #fcd614
• #d06517
• #3b5274
• #f0f0d8
• #382a3a

```html
<!DOCTYPE html>
<html lang="en">
<head>
<meta charset="utf-8">
<title>QM-DR Express Envelope</title>
<link rel="stylesheet" href="https://fonts.googleapis.com/css2?family=Roboto:ital,wght@0,300;0,400;0,700;1,300&display=swap">
<style>
  :root {
    --yellow: #fcd614;
    --yellow-deep: #e2be10;
    --orange: #d06517;
    --blue: #3b5274;
    --cream: #f0f0d8;
    --ink: #221d21;
    --ink-flap: #2a2428;
    --page: #e6e6e6;
    --white: #ffffff;
  }
  * { margin: 0; padding: 0; box-sizing: border-box; }
  html, body { width: 800px; height: 1200px; overflow: hidden; }
  body {
    background: var(--page);
    font-family: "Roboto", Arial, sans-serif;
    color: var(--ink);
    position: relative;
  }

  /* Front side */
  .envelope-front {
    position: absolute; left: 57px; top: 96px; width: 686px; height: 406px;
    background: var(--ink);
    border-radius: 0 32px 32px 0;
    overflow: hidden;
  }
  .stripe { position: absolute; left: 0; right: 0; background: var(--yellow); }
  .stripe-1 { top: 81px; height: 5px; }
  .stripe-2 { top: 92px; height: 2px; }
  .stripe-3 { top: 105px; height: 5px; }
  .stripe-4 { top: 119px; height: 2px; }
  .stripe-5 { top: 130px; height: 6px; }
  .brand-name {
    position: absolute; left: 48px; top: 28px;
    color: var(--yellow); font-weight: 300; font-size: 34px; letter-spacing: 0.5px; line-height: 1;
  }
  .tagline {
    position: absolute; right: 102px; top: 146px;
    color: var(--yellow); font-weight: 300; font-style: italic; font-size: 39px; letter-spacing: -0.5px;
  }
  .bar-orange { position: absolute; left: 0; top: 292px; width: 322px; height: 12px; background: var(--orange); }
  .bar-blue { position: absolute; left: 0; top: 304px; width: 443px; height: 13px; background: var(--blue); }
  .front-band {
    position: absolute; left: 0; right: 0; top: 317px; bottom: 0; background: var(--yellow);
  }
  .product-title {
    position: absolute; left: 48px; top: 14px;
    font-weight: 300; font-size: 40px; letter-spacing: -0.5px; color: var(--ink);
  }
  .front-contact {
    position: absolute; right: 102px; top: 25px; text-align: right;
    font-size: 12.5px; line-height: 18px; color: var(--ink);
  }
  .flap {
    position: absolute; left: 618px; top: 0; bottom: 0; right: 0;
    background: var(--ink-flap);
  }
  .flap-band {
    position: absolute; left: 0; right: 0; top: 317px; bottom: 0;
    background: linear-gradient(90deg, var(--yellow-deep), var(--yellow) 70%);
  }
  .flap-text {
    position: absolute; left: 16px; top: 150px; height: 155px;
    writing-mode: vertical-rl; transform: rotate(180deg);
    color: var(--white); font-size: 7.2px; line-height: 10px;
  }
  .flap-text p:first-child { margin-left: 8px; }
  .flap-text .link { color: var(--yellow); }

  /* Back side */
  .envelope-back {
    position: absolute; left: 57px; top: 695px; width: 686px; height: 407px;
    background: var(--yellow);
  }
  .back-seam {
    position: absolute; left: 0; top: 0; bottom: 0; width: 66px;
    border-radius: 32px 0 0 32px;
    background: linear-gradient(90deg, #f7f7f7, #e9ebea);
  }
  .service-list { position: absolute; left: 102px; top: 37px; font-size: 7px; line-height: 10.6px; }
  .service-list h2 { font-weight: 400; font-size: 12.5px; line-height: 16px; }
  .service-list ul { list-style: none; }
  .service-list li::before { content: "• "; }
  .service-list .continued { display: block; padding-left: 8px; }
  .service-list .visit { font-weight: 700; }
  .doc-notes { position: absolute; left: 102px; top: 204px; font-size: 7px; line-height: 10.6px; }
  .doc-notes .heading { font-weight: 700; }
  .barcode-panel {
    position: absolute; left: 102px; top: 239px; width: 160px; height: 132px; background: var(--white);
  }
  .address-panel {
    position: absolute; left: 385px; top: 213px; width: 265px; height: 159px;
    background: var(--white); font-size: 7px; color: var(--ink);
  }
  .address-panel .field { position: absolute; left: 6px; }
  .rule { position: absolute; background: #555; }
  .rule-sender { left: 6px; right: 0; top: 27px; height: 1px; }
  .rule-state { left: 6px; right: 0; top: 142px; height: 1px; }
  .rule-divider { left: 131px; top: 142px; bottom: 0; width: 1px; }
</style>
</head>
<body>

<section class="envelope-front" aria-label="Envelope front">
  <p class="brand-name">QM-DR</p>
  <div class="stripe stripe-1"></div>
  <div class="stripe stripe-2"></div>
  <div class="stripe stripe-3"></div>
  <div class="stripe stripe-4"></div>
  <div class="stripe stripe-5"></div>
  <p class="tagline">Ship With Trust</p>
  <div class="bar-orange"></div>
  <div class="bar-blue"></div>
  <div class="front-band">
    <h1 class="product-title">Express Envelope</h1>
    <p class="front-contact">1300 584 961<br>www.qmdr.com.au</p>
  </div>
  <div class="flap">
    <div class="flap-band"></div>
    <div class="flap-text">
      <p>Go to <span class="link">www.qmdr.com.au</span> to book your pickup.</p>
      <p>Carried subject to QM-DR Standard Conditions<br>of Carriage; see our website.</p>
    </div>
  </div>
</section>

<section class="envelope-back" aria-label="Envelope back">
  <div class="back-seam"></div>
  <div class="service-list">
    <h2>Ship With Trust</h2>
    <ul>
      <li>Time-guaranteed and next-flight-out service<span class="continued">for vital deliveries</span></li>
      <li>Same-day and next-day local services</li>
      <li>Overnight service to most Australian locations</li>
      <li>Budget road service Australia-wide</li>
      <li>Worldwide express courier</li>
    </ul>
    <p class="visit">Visit www.qmdr.com.au or phone 1300 584 961</p>
  </div>
  <div class="doc-notes">
    <p class="heading">For documents</p>
    <p>• Max weight 500g</p>
    <p>• Max width 20mm</p>
  </div>
  <div class="barcode-panel" aria-label="Blank area for barcode label"></div>
  <div class="address-panel">
    <span class="field" style="top:19px">Sender's name</span>
    <div class="rule rule-sender"></div>
    <span class="field" style="top:38px">Receiver</span>
    <div class="rule rule-state"></div>
    <div class="rule rule-divider"></div>
    <span class="field" style="top:146px">State</span>
    <span class="field" style="top:146px; left:138px">Postcode</span>
  </div>
</section>

</body>
</html>
```